Boat business cards

I'm looking for business cards with the two logos I've attached. I don't have an specific idea in mind and open to anything. All the usual info will be on the card. Name, position in company, nr, email, address, ect. The company rents out these two boats for charters and fishing.

```html
<!DOCTYPE html>
<html lang="en">
<head>
<meta charset="utf-8">
<title>Charter Boat Business Cards</title>
<link href="https://fonts.googleapis.com/css2?family=Roboto:wght@400;500&display=swap" rel="stylesheet">
<style>
  :root {
    --bg: #d4d5d7;
    --card: #ffffff;
    --ink: #3a3d42;
    --blue: #5b8bd6;
    --slate: #5e7494;
    --brown: #8a6a45;
    --grey: #9a9ca0;
    --hull-blue: #8eb0da;
    --hull-brown: #a88760;
  }
  * { box-sizing: border-box; margin: 0; padding: 0; }
  html, body { width: 1200px; height: 800px; overflow: hidden; }
  body {
    background: var(--bg);
    font-family: "Roboto", Arial, sans-serif;
    color: var(--ink);
    position: relative;
  }
  .card {
    position: absolute;
    top: 240px;
    width: 560px;
    height: 320px;
    background: var(--card);
    border-radius: 22px;
    overflow: hidden;
    box-shadow: 0 10px 28px rgba(0,0,0,0.18);
  }
  .card--front { left: 26px; }
  .card--back { left: 614px; }

  .swoosh { position: absolute; left: 0; top: 0; width: 560px; height: 320px; }

  .logo { position: absolute; display: flex; flex-direction: column; align-items: center; }
  .logo__art { border-radius: 4px; }
  .logo__art--blue { background: linear-gradient(100deg, #e9eef5 0%, var(--hull-blue) 55%, #6f93c4 100%); }
  .logo__art--brown { background: linear-gradient(100deg, #eeeae4 0%, var(--hull-brown) 55%, #7e6140 100%); }
  .logo__name {
    font-weight: 500;
    color: var(--ink);
    letter-spacing: 0.5px;
    margin-top: 6px;
  }

  .card--front .logo--seabreeze { left: 40px; top: 40px; }
  .card--front .logo--seabreeze .logo__art { width: 160px; height: 62px; }
  .card--front .logo--silvertide { left: 290px; top: 30px; }
  .card--front .logo--silvertide .logo__art { width: 170px; height: 50px; }
  .card--front .logo__name { font-size: 20px; }

  .person { position: absolute; left: 40px; top: 196px; }
  .person__name { font-size: 22px; font-weight: 500; color: var(--blue); }
  .person__role { font-size: 15px; color: var(--brown); margin-top: 2px; }

  .address { position: absolute; left: 200px; top: 140px; font-size: 13px; line-height: 1.4; font-style: normal; }

  .contact { position: absolute; left: 350px; top: 130px; font-size: 13px; line-height: 1.4; list-style: none; }
  .contact li { display: flex; align-items: center; gap: 6px; }
  .contact svg { width: 11px; height: 11px; flex: none; }

  .card--back .logo { left: 50%; transform: translateX(-50%); }
  .card--back .logo--seabreeze { top: 48px; }
  .card--back .logo--seabreeze .logo__art { width: 230px; height: 72px; }
  .card--back .logo--silvertide { top: 180px; }
  .card--back .logo--silvertide .logo__art { width: 240px; height: 52px; }
  .card--back .logo__name { font-size: 24px; }
</style>
</head>
<body>

<section class="card card--front">
  <svg class="swoosh" viewBox="0 0 560 320" aria-hidden="true">
    <path class="swoosh__base" d="M70 320 C210 304 390 258 560 212 L560 320 Z" fill="var(--slate)"/>
    <path class="swoosh__brown" d="M0 324 C90 304 190 284 300 270 C200 290 100 312 24 326 Z" fill="var(--brown)"/>
    <path class="swoosh__grey" d="M300 272 C400 250 480 224 560 200 L560 206 C480 230 400 256 300 272 Z" fill="var(--grey)"/>
    <path class="swoosh__blue" d="M230 286 C360 256 460 220 560 184 L560 192 C460 228 360 262 230 286 Z" fill="var(--blue)"/>
  </svg>

  <div class="logo logo--seabreeze">
    <div class="logo__art logo__art--blue" role="img" aria-label="Illustration of the Sea Breeze sport fishing boat"></div>
    <span class="logo__name">Sea Breeze</span>
  </div>
  <div class="logo logo--silvertide">
    <div class="logo__art logo__art--brown" role="img" aria-label="Illustration of the Silver Tide motor yacht"></div>
    <span class="logo__name">Silver Tide</span>
  </div>

  <div class="person">
    <p class="person__name">Daniel Reyes</p>
    <p class="person__role">President</p>
  </div>

  <address class="address">
    42 Tidewater Lane<br>Kodiak, Alaska 99615
  </address>

  <ul class="contact">
    <li>
      <svg viewBox="0 0 12 12"><rect x="2.5" y="0.5" width="7" height="11" rx="1.2" fill="none" stroke="var(--blue)" stroke-width="1.2"/></svg>
      555-201-3348
    </li>
    <li>
      <svg viewBox="0 0 12 12"><rect x="0.5" y="2" width="11" height="8" rx="1" fill="var(--blue)"/><path d="M1 3 L6 7 L11 3" fill="none" stroke="#fff" stroke-width="1"/></svg>
      hello@tidewater.com
    </li>
  </ul>
</section>

<section class="card card--back">
  <div class="logo logo--seabreeze">
    <div class="logo__art logo__art--blue" role="img" aria-label="Illustration of the Sea Breeze sport fishing boat"></div>
    <span class="logo__name">Sea Breeze</span>
  </div>
  <div class="logo logo--silvertide">
    <div class="logo__art logo__art--brown" role="img" aria-label="Illustration of the Silver Tide motor yacht"></div>
    <span class="logo__name">Silver Tide</span>
  </div>
</section>

</body>
</html>
```